Startup FinTech / Behavioural Science company needs website redesign

We are a startup company interested in redesigning our website. We have most of our content created already (viewable at www.tallyfern.co), but are interested in an upgraded look and feel. We are happy to adjust content as well based on design input. We will move hosting from hostbirch to webmarlo or similar hosting service, so portability of files is important to us. Our team will have the ability to make minor tweaks/content adjustments, but would look to engage with someone for more-comprehensive enhancements in the future.
Updates

Project Deadline Extended
Reason: Other business needs prevented me from providing timely feedback. I will work on feedback over the next two days but wanted to give additional time for design submissions and revisions.

Target Market(s)

Financial advisors in the US and UK, as well as potential end-users of the tools and potential investors

Industry/Entity Type

Information Technology

Coding

Coded - Design and coding required

Number of Pages Required

1 page

Font styles to use
Sans Serif

Requirements
Must have
• - Lighter, cleaner look and feel. We believe our current website is too heavy and "angular."
• - improved iconography to convey behavioural finance concepts (e.g., herd mentality, and illusion of control)
• - links to social media sites
• - integration with our hostbirch personality profile (viewable now at https://deanmollow.formquill.com/to/qRtZbe. Note: we will change this URL to tallyfern.formquill.com... as a part of the design process)
Nice to have
• - ability for us to add a tab/link to a blog in the future.
• - design that allows us to add additional
• - ability for us to add additional pages (e.g., results from our personality profiles, pages to customize sharing on social media)
• - simple ability to enter an email address to add to our mailing list/request more info
• - mobile-responsive design
Should not have
• - Should not have items like office directions and maps, since we are a virtual team.
• - Contact information (e.g., phone number) should be lower down the page vs. at the top
• - comments boxes or lengthy web forms. A simple name/email address is sufficient.

```html
<!DOCTYPE html>
<html lang="en">
<head>
<meta charset="utf-8">
<title>Tallyfern</title>
<link href="https://fonts.googleapis.com/css2?family=Roboto:wght@300;400;500;700&family=Covered+By+Your+Grace&display=swap" rel="stylesheet">
<style>
:root{
  --purple:#861d9e;
  --purple-soft:#d9a6ea;
  --ink:#222;
  --muted:#555;
  --grey-bg:#efefef;
  --card-bg:#f5f5f7;
  --slate:#3f464d;
  --slate-mid:#474e55;
  --footer:#394047;
  --white:#fff;
}
*{box-sizing:border-box;margin:0;padding:0}
html,body{width:1200px;height:2486px;overflow:hidden}
body{font-family:'Roboto',sans-serif;color:var(--ink);background:var(--white)}
.wrap{width:1100px;margin:0 auto;position:relative}
.section-title{text-align:center;font-size:22px;font-weight:500;color:var(--ink)}
.section-title span{color:var(--purple)}
.dotted{border-top:2px dotted var(--purple);opacity:.7}

/* hero */
.hero{position:relative;height:547px;overflow:hidden}
.hero-photo{position:absolute;inset:0;background:linear-gradient(120deg,#6f757c 0%,#9aa0a6 40%,#7e858c 65%,#5c6168 100%)}
.hero-shade{position:absolute;inset:0;background:rgba(40,44,50,.45)}
.nav{position:absolute;top:0;left:0;right:0;height:70px;border-bottom:1px solid rgba(255,255,255,.25);display:flex;align-items:center;padding:0 50px}
.brand{color:var(--white);font-size:38px;font-weight:500;letter-spacing:.5px;width:300px}
.menu{display:flex;gap:38px;margin-left:62px;list-style:none}
.menu li{color:var(--white);font-size:14px;text-transform:uppercase}
.nav-actions{margin-left:auto;display:flex;gap:8px}
.btn-pill{height:32px;padding:0 12px;border-radius:16px;border:2px solid var(--white);color:var(--white);font-size:13px;font-weight:500;display:flex;align-items:center}
.btn-pill.solid{background:var(--white);color:var(--ink)}
.hero-copy{position:absolute;top:188px;left:0;right:0;text-align:center;color:var(--white)}
.hero-copy h1{font-family:'Covered By Your Grace',cursive;font-weight:400;font-size:44px;line-height:46px;letter-spacing:3px;text-transform:uppercase}
.hero-copy p{font-size:29px;font-weight:300;margin-top:14px;letter-spacing:.5px}
.btn-outline{display:inline-block;margin-top:30px;padding:7px 22px;border:2px solid var(--white);border-radius:6px;font-size:16px;font-weight:500;color:var(--white)}

/* steps */
.steps{height:290px;padding-top:14px}
.steps .dotted{margin-top:10px}
.step-row{display:flex;position:relative;margin-top:26px}
.step{width:275px;text-align:center}
.step-icon{width:95px;height:95px;border-radius:50%;background:var(--purple);margin:0 auto;display:flex;align-items:center;justify-content:center;position:relative;z-index:1}
.step-icon.ring{box-shadow:inset 0 0 0 4px var(--purple),inset 0 0 0 7px var(--white)}
.step-line{position:absolute;top:47px;height:1px;background:#777;width:140px}
.step h3{font-size:17px;font-weight:500;margin-top:28px}
.step.active h3{color:var(--purple)}
.step p{font-size:13px;color:var(--muted);line-height:20px;margin:14px auto 0;width:250px}

/* welcome */
.welcome{background:var(--grey-bg);height:207px}
.welcome .wrap{display:flex;height:100%}
.welcome-text{width:724px;padding-top:18px}
.welcome-text h2{text-align:center;font-size:21px;font-weight:500}
.welcome-text h2 span{color:var(--purple)}
.welcome-text .dotted{margin-top:10px}
.welcome-text p{font-size:13px;line-height:20px;color:#444;text-align:center;margin-top:10px}
.welcome-text p strong{color:var(--purple)}
.traits{display:flex;justify-content:center;gap:36px;list-style:none;margin-top:14px;font-size:13px;color:#444}
.traits li{display:flex;align-items:center;gap:8px}
.welcome-art{margin-left:auto;margin-top:8px;width:350px;height:191px;background:linear-gradient(180deg,#f2e3f7 0%,#e6c2f0 60%,#d9a6ea 100%);border-radius:4px}

/* pillars */
.pillars{display:flex;height:290px}
.pillar{flex:1;background:var(--slate);color:var(--white);text-align:center;padding:22px 48px 0}
.pillar.mid{background:var(--slate-mid)}
.pillar h2{font-size:27px;font-weight:500}
.pillar p{font-size:15px;line-height:22px;margin-top:22px;height:120px}
.btn-box{display:inline-block;margin-top:32px;border:1px solid var(--white);border-radius:3px;padding:10px 18px;font-size:13px;font-weight:500}

/* blog */
.blog{height:464px;padding-top:16px}
.blog .dotted{margin-top:10px}
.cards{display:flex;gap:29px;margin-top:28px}
.card{width:253px;background:var(--card-bg)}
.card-img{height:190px}
.card-body{padding:12px 18px 0;height:166px}
.card h3{font-size:18px;font-weight:500}
.card p{font-size:13px;line-height:20px;color:var(--muted);margin-top:8px}
.card-meta{display:flex;justify-content:space-between;font-size:11px;color:#555;border-top:1px dotted #bbb;margin-top:22px;padding-top:10px}

/* testimonials */
.quotes{background:var(--grey-bg);height:207px;padding-top:16px}
.quotes .dotted{margin-top:10px}
.quote-row{display:flex;margin-top:30px;position:relative}
.quote{display:flex;width:550px;gap:28px;align-items:flex-start}
.quote.left{padding-left:0}
.quote.right{padding-left:38px;flex-direction:row}
.quote-text{font-size:13px;line-height:20px;font-style:italic;color:#666}
.quote.left .quote-text{text-align:right;width:412px}
.quote.right .quote-text{width:412px}
.quote-name{font-size:13px;color:var(--ink);font-style:normal;margin-top:10px}
.quote.left .quote-name{text-align:right}
.avatar{width:76px;height:76px;border-radius:50%;flex:none;background:radial-gradient(circle at 50% 40%,#e3c7b0 0%,#b08a72 55%,#f3f3f3 56%)}
.quote-divider{position:absolute;left:549px;top:0;height:80px;border-left:2px dotted var(--purple)}

/* like bar */
.likebar{height:75px;position:relative}
.likebar .rule{position:absolute;top:37px;left:66px;right:66px;height:1px;background:#ddd}
.like-pill{position:absolute;left:378px;top:17px;width:447px;height:44px;border:1px solid #ddd;border-radius:22px;background:var(--white);display:flex;align-items:center}
.like-thumb{width:56px;height:100%;border-right:1px solid #ddd;display:flex;align-items:center;justify-content:center}
.like-btn{margin-left:64px;background:#4a68a8;color:var(--white);font-size:11px;font-weight:700;padding:3px 6px;border-radius:2px}
.like-text{font-size:11px;color:#333;margin-left:6px}

/* footer */
.footer{background:var(--footer);height:406px;color:var(--white)}
.footer .wrap{padding-top:30px}
.foot-cols{display:flex;justify-content:space-between}
.foot-cols h4{font-size:17px;font-weight:500}
.contact{width:256px}
.contact p{font-size:13px;line-height:20px;margin-top:18px}
.contact .line{font-size:13px;margin-top:14px}
.contact .line b{font-weight:700}
.socials{display:flex;gap:12px;margin-top:18px}
.socials span{width:12px;height:12px;border-radius:50%;background:var(--white)}
.mailer{width:535px;text-align:center}
.field-row{display:flex;gap:24px;margin-top:18px}
.field{flex:1;height:32px;background:var(--white);border-radius:3px;font-size:12px;color:#999;text-align:left;padding:9px 14px}
.field.full{margin-top:18px}
.field.area{height:65px;margin-top:18px}
.btn-send{display:inline-block;margin-top:18px;background:var(--white);color:var(--ink);font-size:12px;font-weight:500;padding:9px 18px;border-radius:3px}
.newsletter{width:254px}
.newsletter p{font-size:13px;line-height:20px;margin-top:18px}
.subscribe{margin-top:24px;height:34px;border-radius:17px;background:#eee;display:flex;align-items:center;font-size:13px;color:#333;padding-left:14px}
.subscribe span{margin-left:auto;background:var(--white);height:34px;width:54px;border-radius:17px;display:flex;align-items:center;justify-content:center}
.foot-bottom{position:absolute;left:0;right:0;top:335px;border-top:1px solid rgba(255,255,255,.3);display:flex;align-items:center;justify-content:space-between;padding-top:18px;font-size:12px;font-weight:500}
.foot-brand{font-size:36px;font-weight:500;position:absolute;left:50%;transform:translateX(-50%);top:8px}
</style>
</head>
<body>

<header class="hero">
  <div class="hero-photo" role="img" aria-label="Photo of hands reviewing financial charts on paper beside a coffee cup"></div>
  <div class="hero-shade"></div>
  <nav class="nav">
    <div class="brand">tallyfern</div>
    <ul class="menu">
      <li>The Problem</li><li>How It Works</li><li>Team</li><li>Blog</li><li>Contact</li>
    </ul>
    <div class="nav-actions">
      <span class="btn-pill">Log In</span>
      <span class="btn-pill solid">Take Profile</span>
    </div>
  </nav>
  <div class="hero-copy">
    <h1>Money Decisions<br>Can Stress You Out</h1>
    <p>Tallyfern Can Help</p>
    <span class="btn-outline">Learn More</span>
  </div>
</header>

<section class="steps">
  <div class="wrap">
    <h2 class="section-title">How <span>It Works</span></h2>
    <div class="dotted"></div>
    <div class="step-row">
      <div class="step-line" style="left:195px"></div>
      <div class="step-line" style="left:470px"></div>
      <div class="step-line" style="left:745px"></div>
      <div class="step">
        <div class="step-icon">
          <svg width="42" height="42" viewBox="0 0 42 42" fill="none" stroke="#fff" stroke-width="2"><rect x="3" y="4" width="36" height="34"/><line x1="3" y1="12" x2="39" y2="12"/><rect x="8" y="17" width="12" height="8"/><line x1="25" y1="18" x2="35" y2="18"/><line x1="25" y1="23" x2="35" y2="23"/><line x1="8" y1="31" x2="35" y2="31"/></svg>
        </div>
        <h3>1. Take the profile</h3>
        <p>Take the Tallyfern profile to learn more about your financial personality and tendencies</p>
      </div>
      <div class="step">
        <div class="step-icon">
          <svg width="44" height="40" viewBox="0 0 44 40" fill="#fff"><circle cx="22" cy="9" r="5"/><circle cx="9" cy="17" r="4"/><circle cx="35" cy="17" r="4"/><path d="M14 30c0-6 4-10 8-10s8 4 8 10z"/><path d="M2 34c0-5 3-9 7-9s7 4 7 9z"/><path d="M28 34c0-5 3-9 7-9s7 4 7 9z"/></svg>
        </div>
        <h3>2. Gain better insight</h3>
        <p>Play the investment simulation to gain better insight into your strengths and weaknesses</p>
      </div>
      <div class="step active">
        <div class="step-icon ring">
          <svg width="44" height="44" viewBox="0 0 44 44" fill="none" stroke="#fff" stroke-width="2"><circle cx="22" cy="9" r="5" fill="#fff"/><path d="M15 30c0-7 3-12 7-12s7 5 7 12z" fill="#fff"/><path d="M4 26l6 6M40 26l-6 6M12 38h20"/></svg>
        </div>
        <h3>3. Connect your accounts</h3>
        <p>Connect your financial accounts to see your opportunities to be a better saver and investor</p>
      </div>
      <div class="step">
        <div class="step-icon">
          <svg width="42" height="40" viewBox="0 0 42 40" fill="none" stroke="#fff" stroke-width="2"><line x1="3" y1="37" x2="39" y2="37"/><rect x="7" y="24" width="5" height="13"/><rect x="16" y="18" width="5" height="19"/><rect x="25" y="21" width="5" height="16"/><rect x="33" y="13" width="5" height="24"/><polyline points="5,16 14,8 23,12 37,3"/></svg>
        </div>
        <h3>4. Check your progress</h3>
        <p>Check your progress over time to stay on track with your business</p>
      </div>
    </div>
  </div>
</section>

<section class="welcome">
  <div class="wrap">
    <div class="welcome-text">
      <h2>Welcome to <span>Tallyfern</span></h2>
      <div class="dotted"></div>
      <p>Each of us has a personality that affects the way we view the world. Similar to how your social personality may influence your interactions with other people, your financial personality can have an impact on the way that you make decisions about money. While there are no "right" or "wrong" personalities, the Tallyfern profile can help you to be more mindful of the financial decisions you make. <strong>Click here to get started</strong></p>
      <ul class="traits">
        <li><svg width="12" height="10" viewBox="0 0 12 10"><path d="M1 5l3.5 3.5L11 1" stroke="#861d9e" stroke-width="2.2" fill="none"/></svg>Short-term Thinking</li>
        <li><svg width="12" height="10" viewBox="0 0 12 10"><path d="M1 5l3.5 3.5L11 1" stroke="#861d9e" stroke-width="2.2" fill="none"/></svg>Herd Mentality</li>
        <li><svg width="12" height="10" viewBox="0 0 12 10"><path d="M1 5l3.5 3.5L11 1" stroke="#861d9e" stroke-width="2.2" fill="none"/></svg>Gambler's Fallacy</li>
        <li><svg width="12" height="10" viewBox="0 0 12 10"><path d="M1 5l3.5 3.5L11 1" stroke="#861d9e" stroke-width="2.2" fill="none"/></svg>Illusion of Control</li>
      </ul>
    </div>
    <div class="welcome-art" role="img" aria-label="Illustration of a desktop computer showing a personality profile on a desk with a pen cup"></div>
  </div>
</section>

<section class="pillars">
  <div class="pillar">
    <h2>Money and Financial</h2>
    <p>This financial stress is among the leading causes of divorce, addiction, obesity and depression. What's worse, the consequences of the decisions that we make can make us even more stressed, not more relieved.</p>
    <span class="btn-box">LEARN MORE</span>
  </div>
  <div class="pillar mid">
    <h2>Ask Anyone</h2>
    <p>the key to good physical health, and you're likely to get a correct answer: don't overeat, choose healthy foods and exercise regularly. The path to good physical health is not a mystery, but we have a hard time following it.</p>
    <span class="btn-box">LEARN MORE</span>
  </div>
  <div class="pillar">
    <h2>Good Financial</h2>
    <p>health works the same way. We generally know what to do – spend less than we earn, save for a rainy day, and make non-emotional investment decisions – but have a hard time doing it.</p>
    <span class="btn-box">LEARN MORE</span>
  </div>
</section>

<section class="blog">
  <div class="wrap">
    <h2 class="section-title">Latest <span>Blog &amp; Views</span></h2>
    <div class="dotted"></div>
    <div class="cards">
      <article class="card">
        <div class="card-img" role="img" aria-label="Photo of a person walking through a doorway carrying a leather bag" style="background:linear-gradient(135deg,#d8d4cf,#6b4a33)"></div>
        <div class="card-body"><h3>Standard Post</h3><p>Enim congue blandit. Lorem ipsum dolor sit amet, consectetur adipiscing elit. Quisque...</p>
        <div class="card-meta"><span>&#9635; 22 June, 2015</span><span>&#9679; 0</span></div></div>
      </article>
      <article class="card">
        <div class="card-img" role="img" aria-label="Photo of a glass coffee carafe on a wooden table" style="background:linear-gradient(160deg,#e8e6e1,#8d7a66)"></div>
        <div class="card-body"><h3>Video Post</h3><p>Ultrices posuere cubilia curae curabitur sit amet tortor ut massa commodo. Vestibulum...</p>
        <div class="card-meta"><span>&#9635; 22 June, 2015</span><span>&#9679; 0</span></div></div>
      </article>
      <article class="card">
        <div class="card-img" role="img" aria-label="Photo of a cafe table and chairs against a brick wall" style="background:linear-gradient(160deg,#7a4a36,#c9b8a8)"></div>
        <div class="card-body"><h3>Post with Image</h3><p>Enim congue blandit. Lorem ipsum dolor sit amet, consectetur adipiscing elit. Quisque...</p>
        <div class="card-meta"><span>&#9635; 22 June, 2015</span><span>&#9679; 0</span></div></div>
      </article>
      <article class="card">
        <div class="card-img" role="img" aria-label="Photo of a leather wallet stuffed with banknotes" style="background:linear-gradient(160deg,#cfc6bb,#6e4c36)"></div>
        <div class="card-body"><h3>Image Post</h3><p>Ultrices posuere cubilia curae curabitur sit amet tortor ut massa commodo. Vestibulum...</p>
        <div class="card-meta"><span>&#9635; 22 June, 2015</span><span>&#9679; 3</span></div></div>
      </article>
    </div>
  </div>
</section>

<section class="quotes">
  <div class="wrap">
    <h2 class="section-title">What <span>People Say</span></h2>
    <div class="dotted"></div>
    <div class="quote-row">
      <div class="quote-divider"></div>
      <div class="quote left">
        <div class="quote-text">Duis aute irure dolor in reprehenderit in voluptate velit esse cillum dolore eu fugiat nulla pariatur. Excepteur sint occaecat cupidatat non proident, sunt in culpa qui officia deserunt mollit.
          <div class="quote-name">Mark Ellery, Operations Manager</div></div>
        <div class="avatar" role="img" aria-label="Portrait photo of Mark Ellery"></div>
      </div>
      <div class="quote right">
        <div class="avatar" role="img" aria-label="Portrait photo of Nora Baines"></div>
        <div class="quote-text">Provident, similique sunt in culpa qui officia deserunt mollitia animi, id est laborum et dolorum fuga. Et harum quidem rerum facilis est et expedita distinctio. Nam libero tempore, cum soluta nobis.
          <div class="quote-name">Nora Baines, Creative Designer</div></div>
      </div>
    </div>
  </div>
</section>

<section class="likebar">
  <div class="rule"></div>
  <div class="like-pill">
    <div class="like-thumb"><svg width="18" height="16" viewBox="0 0 18 16" fill="none" stroke="#bbb" stroke-width="1.5"><rect x="1" y="7" width="4" height="8"/><path d="M5 8l4-6c1.5 0 2 1 1.5 3H16c1 0 1.5 1 1 2l-2 6c-.3.8-1 1-1.6 1H5"/></svg></div>
    <span class="like-btn">&#10003; Like</span>
    <span class="like-text">You and 4k others like this.</span>
  </div>
</section>

<footer class="footer">
  <div class="wrap" style="height:406px">
    <div class="foot-cols">
      <div class="contact">
        <h4>Contact Us</h4>
        <p>Please feel free to contact us for any issue. Our staff is available to you from 9AM until 5PM on weekdays.</p>
        <div class="line"><b>Phone:</b> +1 555 014 2290</div>
        <div class="line"><b>Mobile:</b> +44 7700 900 318</div>
        <div class="line"><b>Email:</b> info@tallyfern.co</div>
        <div class="socials"><span></span><span></span><span></span><span></span><span></span></div>
      </div>
      <div class="mailer">
        <h4>Feel Free to Mail</h4>
        <div class="field-row"><div class="field">Name *</div><div class="field">Email *</div></div>
        <div class="field full">Subject</div>
        <div class="field area">Write Your Message Here...</div>
        <span class="btn-send">SEND MESSAGE</span>
      </div>
      <div class="newsletter">
        <h4>Newsletter Signup</h4>
        <p>Enim congue blandit. Lorem ipsum dolor sit amet, consectetur adipiscing elit. Quisque consectetur interdum finibus. Vestibulum ante ipsum primis in faucibus orci. luctus et ultrices posuere.</p>
        <div class="subscribe">Email address<span>GO</span></div>
      </div>
    </div>
    <div class="foot-bottom">
      <span>Copyright © Tallyfern &amp; Orrin Labs</span>
      <span class="foot-brand">tallyfern</span>
      <span>All rights reserved</span>
    </div>
  </div>
</footer>

</body>
</html>
```